Kelbrook LLC web design project

Dallas, TX based water damage mitigation company needs a web site for its new business. The company does water extractions, mitigation, demo, restoration, and reconstruction. We need for the site to have a strong mobile version, and the owners/managers need to be able to edit the site despite having no web design experience. The site needs to look and function, especially the mobile version, similar to bramfieldorchardworks.com if possible.

```html
<!DOCTYPE html>
<html lang="en">
<head>
<meta charset="utf-8">
<title>Kelbrook LLC – Web Design</title>
<link href="https://fonts.googleapis.com/css2?family=Poppins:wght@400;500;600;700&display=swap" rel="stylesheet">
<style>
:root{
  --slate:#3e4859;
  --blue:#0f72c2;
  --blue-dark:#0b5ea3;
  --ink:#2c3442;
  --muted:#6b7280;
  --light:#f1f1f2;
  --white:#ffffff;
  --gold:#f5b301;
}
*{box-sizing:border-box;margin:0;padding:0}
html,body{width:1200px;height:3783px;overflow:hidden;background:var(--white);font-family:'Poppins',sans-serif;color:var(--ink)}
.abs{position:absolute}
.desk{position:absolute;left:168px;top:91px;width:604px;height:3073px}
.mob{position:absolute;left:857px;top:91px;width:131px;height:3526px}
.ph{position:absolute}
.hero-ph{background:linear-gradient(180deg,#7fb0db 0%,#a9cbe6 45%,#6f8d5a 62%,#7d98a4 78%,#5b7381 100%)}
.pipe-ph{background:linear-gradient(180deg,rgba(255,255,255,1) 0%,rgba(234,238,240,1) 45%,#c9d2cf 65%,#9aa890 82%,#7c8e5f 100%)}
.pill{position:absolute;border-radius:999px;background:var(--blue);color:var(--white);display:flex;align-items:center;justify-content:center;font-weight:600;text-align:center}
.phone-pill{background:var(--blue-dark);justify-content:flex-start;gap:4px;padding-left:5px}
.phone-pill .dot{width:12px;height:12px;border-radius:50%;background:var(--white)}
.phone-pill small{display:block;font-size:4px;font-weight:500;line-height:1}
.phone-pill b{display:block;font-size:7px;line-height:1.1}
.brand{position:absolute;font-weight:700;color:var(--blue);text-align:center;letter-spacing:.5px}
.menu-dot{position:absolute;border-radius:50%;background:var(--slate)}
.h2{position:absolute;font-weight:600;text-transform:uppercase;line-height:1.1}
.p{position:absolute;line-height:1.45;color:var(--muted)}
.on-dark{color:var(--white)}
.card{position:absolute;background:var(--white);box-shadow:0 2px 8px rgba(0,0,0,.12);text-align:center}
.card .img{position:absolute;left:0;top:0;width:100%}
.card h4{position:absolute;left:0;width:100%;font-weight:600;text-transform:uppercase;color:var(--ink)}
.card p{position:absolute;left:8%;width:84%;color:var(--muted);line-height:1.45}
.outline-btn{position:absolute;border:1.5px solid var(--blue);color:var(--blue);border-radius:999px;font-weight:600;display:flex;align-items:center;justify-content:center}
.arrow{position:absolute;color:var(--white);font-size:16px;font-weight:500}
.step{position:absolute;text-align:center}
.step .num{font-size:26px;font-weight:500;color:transparent;-webkit-text-stroke:1px #9aa3ae;line-height:1}
.step h5{font-size:10px;font-weight:600;margin-top:4px}
.step p{font-size:6.5px;color:var(--muted);line-height:1.4;margin-top:4px}
.price-item{position:absolute;color:var(--white)}
.price-item h6{font-size:8px;font-weight:600;text-transform:uppercase}
.price-item p{font-size:6.5px;line-height:1.4;margin-top:2px}
.icon{position:absolute}
.review{position:absolute;background:var(--white);box-shadow:0 2px 8px rgba(0,0,0,.12)}
.review .av{position:absolute;border-radius:50%;background:#8a96a5}
.review .nm{position:absolute;font-weight:600}
.review .dt{position:absolute;color:var(--muted)}
.review .st{position:absolute;color:var(--gold);letter-spacing:1px}
.review .gc{position:absolute;border-radius:50%;border:2px solid var(--blue)}
.review p{position:absolute;color:var(--muted);line-height:1.4}
.blog-date{position:absolute;left:0;width:100%;color:var(--blue);font-weight:600}
.areas{position:absolute;list-style:none}
.areas li{display:flex;align-items:center;gap:4px;color:var(--muted)}
.areas li::before{content:"";width:3px;height:7px;background:var(--blue);transform:skewX(-20deg)}
.foot-h{position:absolute;font-weight:600;color:var(--white);text-transform:uppercase}
.foot-t{position:absolute;color:#d6dbe2;line-height:1.5}
.field{position:absolute;background:#4d5869;border-radius:999px;color:#cfd5dd;display:flex;align-items:center}
.dots{position:absolute;display:flex;gap:5px;justify-content:center}
.dots i{width:4px;height:4px;border-radius:50%;background:#bcd3ea}
.dots i.on{background:var(--blue)}
</style>
</head>
<body>

<!-- ================= DESKTOP ================= -->
<main class="desk">

  <!-- Hero -->
  <section class="ph hero-ph" style="left:0;top:0;width:604px;height:335px" role="img" aria-label="Photo of an elephant spraying water in a river under a blue sky"></section>
  <div class="pill phone-pill" style="left:66px;top:34px;width:98px;height:24px"><span class="dot"></span><span><small>CLICK TO CALL</small><b>555 014 2277</b></span></div>
  <div class="brand" style="left:232px;top:46px;width:140px;font-size:17px">KELBROOK<div style="font-size:6px;letter-spacing:3px;color:var(--slate)">LLC</div></div>
  <div class="menu-dot" style="left:517px;top:36px;width:20px;height:20px"></div>
  <div class="pill" style="left:66px;top:297px;width:473px;height:74px;font-size:17px;letter-spacing:.3px">WATER DAMAGE &amp; RESTORATION SERVICES</div>

  <!-- About -->
  <section class="ph pipe-ph" style="left:0;top:406px;width:604px;height:300px" role="img" aria-label="Photo of water gushing from a pipe onto a grassy field"></section>
  <h2 class="h2" style="left:271px;top:440px;font-size:24px">About Us</h2>
  <p class="p" style="left:271px;top:472px;width:256px;font-size:7.5px;color:var(--ink)">Lorem ipsum dolor sit amet, consectetur adipiscing elit, sed do eiusmod tempor incididunt ut labore et dolore magna aliqua. Quis ipsum suspendisse ultrices gravida. Risus commodo viverra maecenas accumsan lacus vel facilisis. Lorem ipsum dolor sit amet, consectetur adipiscing elit, sed do eiusmod tempor incididunt ut labore et dolore magna aliqua. Quis ipsum suspendisse ultrices gravida. Risus commodo</p>

  <!-- Services -->
  <section class="abs" style="left:0;top:706px;width:604px;height:232px;background:var(--slate)"></section>
  <h2 class="h2 on-dark" style="left:66px;top:745px;font-size:22px">Our<br>Services</h2>
  <p class="p on-dark" style="left:232px;top:757px;width:304px;font-size:7.5px">Lorem ipsum dolor sit amet, consectetur adipiscing elit, sed do eiusmod tempor incididunt ut labore et dolore magna aliqua. Quis ipsum suspendisse ultrices gravida. Risus commodo viverra maecenas accumsan lacus vel facilisis.</p>
  <span class="arrow" style="left:28px;top:866px">&#8249;</span>
  <span class="arrow" style="left:567px;top:866px">&#8250;</span>

  <article class="card" style="left:66px;top:835px;width:146px;height:267px">
    <div class="img ph" style="height:103px;background:linear-gradient(135deg,#8fb6d8,#c7a46a 60%,#6c7a4e)" role="img" aria-label="Photo of muddy water pouring from a large pipe"></div>
    <h4 style="top:121px;font-size:9px">Water Extractions</h4>
    <p style="top:146px;font-size:6.5px">Lorem ipsum dolor sit amet, consectetur adipiscing elit, sed do eiusmod tempor incididunt ut labore et dolore mislogna aliqua. Quis ipsum suspendis eultrices gravida. Risus com modo viverra max.</p>
    <div class="outline-btn" style="left:35px;top:231px;width:76px;height:18px;font-size:6.5px">READ MORE</div>
  </article>
  <article class="card" style="left:230px;top:835px;width:146px;height:267px">
    <div class="img ph" style="height:103px;background:linear-gradient(135deg,#b7c2cf,#d8dde3 50%,#7f8da0)" role="img" aria-label="Photo of a technician repairing a pipe fitting"></div>
    <h4 style="top:121px;font-size:9px">Mitigation</h4>
    <p style="top:146px;font-size:6.5px">Lorem ipsum dolor sit amet, consectetur adipiscing elit, sed do eiusmod tempor incididunt ut labore et dolore mislogna aliqua. Quis ipsum suspendis eultrices gravida. Risus com modo viverra max.</p>
    <div class="outline-btn" style="left:35px;top:231px;width:76px;height:18px;font-size:6.5px">READ MORE</div>
  </article>
  <article class="card" style="left:394px;top:835px;width:146px;height:267px">
    <div class="img ph" style="height:103px;background:linear-gradient(135deg,#a6c27a,#6e8f4a 55%,#4e5d45)" role="img" aria-label="Photo of water spurting from a broken pipe in a field"></div>
    <h4 style="top:121px;font-size:9px">Restoration</h4>
    <p style="top:146px;font-size:6.5px">Lorem ipsum dolor sit amet, consectetur adipiscing elit, sed do eiusmod tempor incididunt ut labore et dolore mislogna aliqua. Quis ipsum suspendis eultrices gravida. Risus com modo viverra max.</p>
    <div class="outline-btn" style="left:35px;top:231px;width:76px;height:18px;font-size:6.5px">READ MORE</div>
  </article>

  <!-- Three ways -->
  <h2 class="h2" style="left:0;top:1171px;width:604px;text-align:center;font-size:22px">3 Simple Ways to Get<br>Your Estimate Today!</h2>
  <div class="step" style="left:66px;top:1266px;width:146px"><div class="num">01</div><h5>CALL US</h5><p>Lorem ipsum dolor sit amet, consect adipiscing elit, sed do eiusmod tempor incididunt ut labore et doloreema</p></div>
  <div class="step" style="left:230px;top:1266px;width:146px"><div class="num">02</div><h5>TEXT US</h5><p>Lorem ipsum dolor sit amet, consect adipiscing elit, sed do eiusmod tempor incididunt ut labore et doloreema</p></div>
  <div class="step" style="left:394px;top:1266px;width:146px"><div class="num">03</div><h5>EMAIL US</h5><p>Lorem ipsum dolor sit amet, consect adipiscing elit, sed do eiusmod tempor incididunt ut labore et doloreema</p></div>
  <div class="pill" style="left:93px;top:1372px;width:92px;height:22px;font-size:7px">CLICK TO CALL</div>
  <div class="pill" style="left:257px;top:1372px;width:92px;height:22px;font-size:7px">CLICK TO TEXT</div>
  <div class="pill" style="left:421px;top:1372px;width:92px;height:22px;font-size:7px">CLICK TO EMAIL</div>

  <!-- How we price -->
  <section class="abs" style="left:0;top:1479px;width:604px;height:309px;background:var(--blue)"></section>
  <h2 class="h2 on-dark" style="left:0;top:1526px;width:604px;text-align:center;font-size:22px">How We Price</h2>
  <div class="price-item" style="left:44px;top:1577px;width:148px;text-align:right"><h6>Lorensum Dummy</h6><p>Lorem ipsum dolor sit amet, consectetur adipiselit, sed do eiusmod tempor cididunt ut labore et dolore mislogna aliqua.</p></div>
  <div class="price-item" style="left:44px;top:1635px;width:148px;text-align:right"><h6>Lorensum Dummy</h6><p>Lorem ipsum dolor sit amet, consectetur adipiselit, sed do eiusmod tempor cididunt ut labore et dolore mislogna aliqua.</p></div>
  <div class="price-item" style="left:44px;top:1692px;width:148px;text-align:right"><h6>Lorensum Dummy</h6><p>Lorem ipsum dolor sit amet, consectetur adipiselit, sed do eiusmod tempor cididunt ut labore et dolore mislogna aliqua.</p></div>
  <div class="price-item" style="left:422px;top:1577px;width:148px"><h6>Lorensum Dummy</h6><p>Lorem ipsum dolor sit amet, consectetur adipiselit, sed do eiusmod tempor cididunt ut labore et dolore mislogna aliqua.</p></div>
  <div class="price-item" style="left:422px;top:1635px;width:148px"><h6>Lorensum Dummy</h6><p>Lorem ipsum dolor sit amet, consectetur adipiselit, sed do eiusmod tempor cididunt ut labore et dolore mislogna aliqua.</p></div>
  <div class="price-item" style="left:422px;top:1692px;width:148px"><h6>Lorensum Dummy</h6><p>Lorem ipsum dolor sit amet, consectetur adipiselit, sed do eiusmod tempor cididunt ut labore et dolore mislogna aliqua.</p></div>
  <svg class="icon" style="left:202px;top:1579px" width="14" height="14" viewBox="0 0 14 14"><circle cx="7" cy="7" r="5" fill="none" stroke="#fff" stroke-width="3" stroke-dasharray="2.5 1.4"/><circle cx="7" cy="7" r="2" fill="#fff"/></svg>
  <svg class="icon" style="left:202px;top:1636px" width="14" height="14" viewBox="0 0 14 14"><path d="M4 6V4.5a3 3 0 0 1 6 0V6" fill="none" stroke="#fff" stroke-width="1.6"/><rect x="2.5" y="6" width="9" height="7" rx="1" fill="#fff"/></svg>
  <svg class="icon" style="left:202px;top:1693px" width="14" height="14" viewBox="0 0 14 14"><circle cx="7" cy="6" r="4.5" fill="#fff"/><rect x="5" y="10" width="4" height="3" fill="#fff"/></svg>
  <svg class="icon" style="left:402px;top:1579px" width="14" height="14" viewBox="0 0 14 14"><path d="M1 7L13 1L9 13L7 8Z" fill="#fff"/></svg>
  <svg class="icon" style="left:402px;top:1636px" width="14" height="14" viewBox="0 0 14 14"><path d="M2 12L3 9L10 2L12 4L5 11Z" fill="#fff"/></svg>
  <svg class="icon" style="left:402px;top:1693px" width="14" height="14" viewBox="0 0 14 14"><path d="M1 7L13 1L9 13L7 8Z" fill="#fff"/></svg>

  <!-- Reviews -->
  <div class="abs" style="left:214px;top:1846px;width:28px;height:28px;border-radius:50%;border:5px solid var(--blue)"></div>
  <div class="abs" style="left:250px;top:1846px;font-size:12px;font-weight:600;line-height:1.2;color:var(--slate)">Verified<br>Customer Reviews</div>

  <div class="review" style="left:66px;top:1909px;width:146px;height:110px">
    <span class="av" style="left:20px;top:15px;width:16px;height:16px"></span>
    <span class="nm" style="left:42px;top:15px;font-size:5.5px">Marla Fenwick</span>
    <span class="dt" style="left:42px;top:22px;font-size:5px">2021-02-12</span>
    <span class="gc" style="left:118px;top:15px;width:10px;height:10px"></span>
    <span class="st" style="left:18px;top:34px;font-size:8px">★★★★★</span>
    <p style="left:18px;top:55px;width:110px;font-size:6px">Lorem ipsum dolor sit amet, consectetur adipiscing elit, sed do eiusmod tempor incididunt ut labore et dolore magna</p>
  </div>
  <div class="review" style="left:228px;top:1909px;width:146px;height:110px">
    <span class="av" style="left:20px;top:15px;width:16px;height:16px"></span>
    <span class="nm" style="left:42px;top:15px;font-size:5.5px">Marla Fenwick</span>
    <span class="dt" style="left:42px;top:22px;font-size:5px">2021-02-12</span>
    <span class="gc" style="left:118px;top:15px;width:10px;height:10px"></span>
    <span class="st" style="left:18px;top:34px;font-size:8px">★★★★★</span>
    <p style="left:18px;top:55px;width:110px;font-size:6px">Lorem ipsum dolor sit amet, consectetur adipiscing elit, sed do eiusmod tempor incididunt ut labore et dolore magna</p>
  </div>
  <div class="review" style="left:389px;top:1909px;width:146px;height:110px">
    <span class="av" style="left:20px;top:15px;width:16px;height:16px"></span>
    <span class="nm" style="left:42px;top:15px;font-size:5.5px">Marla Fenwick</span>
    <span class="dt" style="left:42px;top:22px;font-size:5px">2021-02-12</span>
    <span class="gc" style="left:118px;top:15px;width:10px;height:10px"></span>
    <span class="st" style="left:18px;top:34px;font-size:8px">★★★★★</span>
    <p style="left:18px;top:55px;width:110px;font-size:6px">Lorem ipsum dolor sit amet, consectetur adipiscing elit, sed do eiusmod tempor incididunt ut labore et dolore magna</p>
  </div>

  <!-- Blog -->
  <section class="abs" style="left:0;top:2075px;width:604px;height:358px;background:var(--light)"></section>
  <h2 class="h2" style="left:0;top:2122px;width:604px;text-align:center;font-size:21px">Latest Blog Posts</h2>
  <article class="card" style="left:66px;top:2164px;width:146px;height:223px">
    <div class="img ph" style="height:103px;background:linear-gradient(135deg,#7b8b5a,#c9a35c 55%,#8a7a50)" role="img" aria-label="Photo of water flooding over grass"></div>
    <h4 style="top:112px;font-size:8.5px;text-transform:none;line-height:1.3">Lorem ipsum dolor sit<br>amet, consectetur</h4>
    <p style="top:148px;font-size:6.5px">Lorem ipsum dolor sit amet, consectetur adipiscing elit, sed do eiusmod tempor incidid</p>
    <span class="blog-date" style="top:190px;font-size:6.5px">FEB 20 2022</span>
  </article>
  <article class="card" style="left:228px;top:2164px;width:146px;height:223px">
    <div class="img ph" style="height:103px;background:linear-gradient(135deg,#4f7a3a,#8cb35c 55%,#3c5a2e)" role="img" aria-label="Photo of a hose spraying water on green grass"></div>
    <h4 style="top:112px;font-size:8.5px;text-transform:none;line-height:1.3">Lorem ipsum dolor sit<br>amet, consectetur</h4>
    <p style="top:148px;font-size:6.5px">Lorem ipsum dolor sit amet, consectetur adipiscing elit, sed do eiusmod tempor incidid</p>
    <span class="blog-date" style="top:190px;font-size:6.5px">FEB 20 2022</span>
  </article>
  <article class="card" style="left:389px;top:2164px;width:146px;height:223px">
    <div class="img ph" style="height:103px;background:linear-gradient(135deg,#d9dcdf,#8a9098 50%,#2f3a33)" role="img" aria-label="Photo of white plumbing pipes and a pump"></div>
    <h4 style="top:112px;font-size:8.5px;text-transform:none;line-height:1.3">Lorem ipsum dolor sit<br>amet, consectetur</h4>
    <p style="top:148px;font-size:6.5px">Lorem ipsum dolor sit amet, consectetur adipiscing elit, sed do eiusmod tempor incidid</p>
    <span class="blog-date" style="top:190px;font-size:6.5px">FEB 20 2022</span>
  </article>

  <!-- Service areas -->
  <svg class="abs" style="left:66px;top:2480px" width="232" height="261" viewBox="0 0 232 261" role="img" aria-label="Street map of the service region in a hexagon frame">
    <defs><linearGradient id="mapD" x1="0" y1="0" x2="1" y2="1"><stop offset="0" stop-color="#e8e4dc"/><stop offset="1" stop-color="#d6dde3"/></linearGradient></defs>
    <polygon points="116,0 232,65 232,196 116,261 0,196 0,65" fill="url(#mapD)"/>
  </svg>
  <h2 class="h2" style="left:323px;top:2529px;font-size:22px">Service Areas</h2>
  <p class="p" style="left:323px;top:2561px;width:228px;font-size:7px">Lorem ipsum dolor sit amet, consectetur adipiscing elit, sed do eiusmod tempor incididunt ut labore et dolore magna aliqua. Quis ipsum suspendisse ultrices gravi sus commodo viverra maecenas accumsan</p>
  <ul class="areas" style="left:336px;top:2614px;font-size:7px;line-height:16px"><li>Boise</li><li>Meridian</li><li>Eagle</li><li>Star</li><li>Nampa</li></ul>
  <ul class="areas" style="left:402px;top:2614px;font-size:7px;line-height:16px"><li>Caldwell</li><li>Middleton</li><li>Garden City</li><li>Kuna</li><li>Emmett</li></ul>

  <!-- Footer -->
  <footer class="abs" style="left:0;top:2755px;width:604px;height:318px;background:var(--slate)">
    <svg class="abs" style="left:0;top:0" width="604" height="96" viewBox="0 0 604 96"><polygon points="0,0 604,0 604,1 302,95 0,1" fill="#fff"/></svg>
    <div class="brand" style="left:56px;top:184px;width:120px;font-size:19px;color:var(--white)">KELBROOK<div style="font-size:6px;letter-spacing:3px">LLC</div></div>
    <div class="foot-h" style="left:199px;top:146px;font-size:8px">Contact Us</div>
    <svg class="abs" style="left:199px;top:171px" width="8" height="10" viewBox="0 0 8 10"><path d="M4 10C1 6 0 4.5 0 3.5a4 4 0 0 1 8 0C8 4.5 7 6 4 10Z" fill="var(--blue)"/><circle cx="4" cy="3.6" r="1.4" fill="var(--slate)"/></svg>
    <div class="foot-t" style="left:214px;top:168px;font-size:6.5px">Loremu suodu dummy<br>984 dummy 094 dumm<br>Stree lor 6849</div>
    <svg class="abs" style="left:199px;top:215px" width="8" height="9" viewBox="0 0 8 9"><path d="M1 0.5L3 0.5L3.6 2.6L2.6 3.4C3.1 4.7 4 5.6 5.3 6.1L6.1 5.1L8 5.7L8 7.7C4 8.5 0 4.5 1 0.5Z" fill="var(--blue)"/></svg>
    <div class="foot-t" style="left:214px;top:213px;font-size:6.5px">Phone:<br>0 5550 1473 286<br>0 5550 1473 287</div>
    <div class="foot-h" style="left:336px;top:146px;font-size:8px">Links</div>
    <div class="foot-t" style="left:336px;top:168px;font-size:6.5px;width:70px">Lorem ipsum dol amet, consectetur dd do eiusmod tiempor lorem ncididunt ut labor get dol magna aliquipsum disse ultricida.</div>
    <div class="foot-h" style="left:442px;top:146px;font-size:8px">Newsletter</div>
    <div class="field" style="left:442px;top:168px;width:98px;height:18px;padding-left:10px;font-size:6px">Username</div>
    <div class="field" style="left:442px;top:194px;width:98px;height:18px;padding-left:10px;font-size:6px">Email</div>
    <div class="pill" style="left:442px;top:229px;width:98px;height:20px;font-size:6.5px">SUBMIT HERE</div>
    <div class="foot-t" style="left:0;top:292px;width:604px;text-align:center;font-size:6px">© Copyright ® 2022 All rights reserved.</div>
  </footer>
</main>

<!-- ================= MOBILE ================= -->
<main class="mob">

  <section class="ph hero-ph" style="left:0;top:0;width:131px;height:195px" role="img" aria-label="Photo of an elephant spraying water in a river"></section>
  <div class="pill phone-pill" style="left:28px;top:10px;width:75px;height:16px;gap:3px;padding-left:4px"><span class="dot" style="width:9px;height:9px"></span><span><small style="font-size:3px">CLICK TO CALL</small><b style="font-size:5.5px">555 014 2277</b></span></div>
  <div class="brand" style="left:20px;top:60px;width:90px;font-size:12px">KELBROOK<div style="font-size:4px;letter-spacing:2px;color:var(--slate)">LLC</div></div>
  <div class="menu-dot" style="left:111px;top:63px;width:12px;height:12px"></div>
  <div class="pill" style="left:12px;top:181px;width:107px;height:28px;font-size:6.5px;line-height:1.3">WATER DAMAGE &amp;<br>RESTORATION SERVICES</div>

  <h2 class="h2" style="left:15px;top:318px;font-size:11px">About Us</h2>
  <p class="p" style="left:15px;top:340px;width:106px;font-size:5.5px;color:var(--ink)">Lorem ipsum dolor sit amet, consectetur adipiscing elit, sed do eiusmod tempor incididunt ut labore et dolore magna ut aa. Quis ipsum suspendisse ultrices gravida. Risus comm odo viverra maecenas accu msan lacus vel facilisislorem ipsum dolor slame consectetur adipiscin</p>
  <section class="ph pipe-ph" style="left:0;top:410px;width:131px;height:99px;background:linear-gradient(180deg,#eef1f2,#c5cfcc 50%,#8c9b73)" role="img" aria-label="Photo of water gushing from a pipe"></section>

  <section class="abs" style="left:0;top:509px;width:131px;height:231px;background:var(--slate)"></section>
  <h2 class="h2 on-dark" style="left:15px;top:528px;font-size:11px">Our<br>Services</h2>
  <p class="p on-dark" style="left:15px;top:563px;width:104px;font-size:5.5px">Lorem ipsum dolor sit amet, consectetur adipiscing elit, sed do eiusmod tempor incididunt ut labore et dolore magna aliqua. Quis ipsum suspendi se ultrices gravida</p>
  <span class="arrow" style="left:3px;top:690px;font-size:11px">&#8249;</span>
  <span class="arrow" style="left:121px;top:690px;font-size:11px">&#8250;</span>
  <article class="card" style="left:13px;top:638px;width:104px;height:244px">
    <div class="img ph" style="height:102px;background:linear-gradient(135deg,#7b8b5a,#c9a35c 55%,#8a7a50)" role="img" aria-label="Photo of muddy water pouring from a pipe"></div>
    <h4 style="top:114px;font-size:6.5px;line-height:1.3">Water<br>Extractions</h4>
    <p style="top:140px;font-size:5px">Lorem ipsum dolor sit amet, consectetur adipiscing elit, sed do eiusmod tempor incididunt ut labore et dolore mislogna aliqua. Quis ipsum suspendisseultricesda.</p>
  </article>

  <h2 class="h2" style="left:0;top:917px;width:131px;text-align:center;font-size:7.5px">3 Simple<br>Ways to Get Your<br>Estimate Today!</h2>
  <div class="step" style="left:8px;top:977px;width:115px"><div class="num" style="font-size:20px">01</div><h5 style="font-size:7.5px">CALL US</h5><p style="font-size:5.5px">Lorem ipsum dolor sit amet, consect adipiscing elit, sed do eiusmod tempor incididunt ut labore et doloreema</p></div>
  <div class="pill" style="left:18px;top:1084px;width:95px;height:19px;font-size:5.5px">CLICK TO CALL</div>
  <div class="dots" style="left:0;top:1131px;width:131px"><i class="on"></i><i></i><i></i></div>

  <section class="abs" style="left:0;top:1154px;width:131px;height:458px;background:var(--blue)"></section>
  <h2 class="h2 on-dark" style="left:15px;top:1180px;font-size:9px">How We Price</h2>
  <div class="price-item" style="left:34px;top:1210px;width:88px"><h6 style="font-size:5.5px">Lorensum Dummy</h6><p style="font-size:4.8px">Lorem ipsum dolor sit amet, consectetur adipiselit, sed do eiusmod tempor cididunt ut labore et dolore</p></div>
  <div class="price-item" style="left:34px;top:1274px;width:88px"><h6 style="font-size:5.5px">Lorensum Dummy</h6><p style="font-size:4.8px">Lorem ipsum dolor sit amet, consectetur adipiselit, sed do eiusmod tempor cididunt ut labore et dolore</p></div>
  <div class="price-item" style="left:34px;top:1340px;width:88px"><h6 style="font-size:5.5px">Lorensum Dummy</h6><p style="font-size:4.8px">Lorem ipsum dolor sit amet, consectetur adipiselit, sed do eiusmod tempor cididunt ut labore et dolore</p></div>
  <div class="price-item" style="left:34px;top:1406px;width:88px"><h6 style="font-size:5.5px">Lorensum Dummy</h6><p style="font-size:4.8px">Lorem ipsum dolor sit amet, consectetur adipiselit, sed do eiusmod tempor cididunt ut labore et dolore</p></div>
  <div class="price-item" style="left:34px;top:1469px;width:88px"><h6 style="font-size:5.5px">Lorensum Dummy</h6><p style="font-size:4.8px">Lorem ipsum dolor sit amet, consectetur adipiselit, sed do eiusmod tempor cididunt ut labore et dolore</p></div>
  <div class="price-item" style="left:34px;top:1534px;width:88px"><h6 style="font-size:5.5px">Lorensum Dummy</h6><p style="font-size:4.8px">Lorem ipsum dolor sit amet, consectetur adipiselit, sed do eiusmod tempor cididunt ut labore et dolore</p></div>
  <svg class="icon" style="left:11px;top:1212px" width="14" height="14" viewBox="0 0 14 14"><circle cx="7" cy="7" r="5" fill="none" stroke="#fff" stroke-width="3" stroke-dasharray="2.5 1.4"/><circle cx="7" cy="7" r="2" fill="#fff"/></svg>
  <svg class="icon" style="left:11px;top:1276px" width="14" height="14" viewBox="0 0 14 14"><path d="M4 6V4.5a3 3 0 0 1 6 0V6" fill="none" stroke="#fff" stroke-width="1.6"/><rect x="2.5" y="6" width="9" height="7" rx="1" fill="#fff"/></svg>
  <svg class="icon" style="left:11px;top:1342px" width="14" height="14" viewBox="0 0 14 14"><circle cx="7" cy="6" r="4.5" fill="#fff"/><rect x="5" y="10" width="4" height="3" fill="#fff"/></svg>
  <svg class="icon" style="left:11px;top:1408px" width="14" height="14" viewBox="0 0 14 14"><path d="M1 7L13 1L9 13L7 8Z" fill="#fff"/></svg>
  <svg class="icon" style="left:11px;top:1471px" width="14" height="14" viewBox="0 0 14 14"><path d="M2 12L3 9L10 2L12 4L5 11Z" fill="#fff"/></svg>
  <svg class="icon" style="left:11px;top:1536px" width="14" height="14" viewBox="0 0 14 14"><path d="M1 7L13 1L9 13L7 8Z" fill="#fff"/></svg>

  <div class="abs" style="left:13px;top:1633px;width:22px;height:22px;border-radius:50%;border:4px solid var(--blue)"></div>
  <div class="abs" style="left:40px;top:1634px;font-size:6.5px;font-weight:600;line-height:1.25;color:var(--slate)">Verified<br>Customer Reviews</div>
  <div class="review" style="left:9px;top:1675px;width:111px;height:85px">
    <span class="av" style="left:12px;top:10px;width:12px;height:12px"></span>
    <span class="nm" style="left:28px;top:10px;font-size:4.5px">Marla Fenwick</span>
    <span class="dt" style="left:28px;top:16px;font-size:4px">2021-02-12</span>
    <span class="gc" style="left:92px;top:10px;width:8px;height:8px"></span>
    <span class="st" style="left:11px;top:25px;font-size:6px">★★★★★</span>
    <p style="left:11px;top:42px;width:88px;font-size:4.5px">Lorem ipsum dolor sit amet, consectetur adipiscing elit, sed do eiusmod tempor incididunt ut labore et dolore magna</p>
  </div>
  <div class="dots" style="left:0;top:1778px;width:131px;gap:4px"><i class="on" style="width:3px;height:3px"></i><i class="on" style="width:3px;height:3px"></i><i class="on" style="width:3px;height:3px"></i><i class="on" style="width:3px;height:3px"></i><i class="on" style="width:3px;height:3px"></i><i class="on" style="width:3px;height:3px"></i><i class="on" style="width:3px;height:3px"></i></div>

  <section class="abs" style="left:0;top:1800px;width:131px;height:290px;background:var(--light)"></section>
  <h2 class="h2" style="left:0;top:1818px;width:131px;text-align:center;font-size:9px">Latest<br>Blog Posts</h2>
  <article class="card" style="left:9px;top:1862px;width:111px;height:220px">
    <div class="img ph" style="height:102px;background:linear-gradient(135deg,#7b8b5a,#c9a35c 55%,#8a7a50)" role="img" aria-label="Photo of water flooding over grass"></div>
    <h4 style="top:118px;font-size:6.5px;text-transform:none;line-height:1.3">Lorem ipsum dolor sit<br>amet, consectetur</h4>
    <p style="top:148px;font-size:5.2px">Lorem ipsum dolor sit amet, consectetur adipiscing elit, sed do eiusmod tempor incidid</p>
    <span class="blog-date" style="top:192px;font-size:5.5px">FEB 20 2022</span>
  </article>
  <article class="card" style="left:9px;top:2101px;width:111px;height:222px">
    <div class="img ph" style="height:102px;background:linear-gradient(135deg,#4f7a3a,#8cb35c 55%,#3c5a2e)" role="img" aria-label="Photo of a hose spraying water on grass"></div>
    <h4 style="top:118px;font-size:6.5px;text-transform:none;line-height:1.3">Lorem ipsum dolor sit<br>amet, consectetur</h4>
    <p style="top:148px;font-size:5.2px">Lorem ipsum dolor sit amet, consectetur adipiscing elit, sed do eiusmod tempor incidid</p>
    <span class="blog-date" style="top:194px;font-size:5.5px">FEB 20 2022</span>
  </article>
  <article class="card" style="left:9px;top:2342px;width:111px;height:223px">
    <div class="img ph" style="height:102px;background:linear-gradient(135deg,#d9dcdf,#8a9098 50%,#2f3a33)" role="img" aria-label="Photo of plumbing pipes and a pump"></div>
    <h4 style="top:118px;font-size:6.5px;text-transform:none;line-height:1.3">Lorem ipsum dolor sit<br>amet, consectetur</h4>
    <p style="top:148px;font-size:5.2px">Lorem ipsum dolor sit amet, consectetur adipiscing elit, sed do eiusmod tempor incidid</p>
    <span class="blog-date" style="top:195px;font-size:5.5px">FEB 20 2022</span>
  </article>

  <h2 class="h2" style="left:15px;top:2606px;font-size:9px">Service Areas</h2>
  <p class="p" style="left:15px;top:2624px;width:106px;font-size:5px">Lorem ipsum dolor sit amet, consectetur adipiscing elit, sed do eiusmod tempor incididunt ut labore et dolore magna aliqua. Quis ipsum suspendisse ultrices gravi sus commodo viverra maecenas accumsan</p>
  <ul class="areas" style="left:18px;top:2700px;font-size:5px;line-height:15px"><li>Boise</li><li>Meridian</li><li>Eagle</li><li>Star</li><li>Nampa</li></ul>
  <ul class="areas" style="left:72px;top:2700px;font-size:5px;line-height:15px"><li>Caldwell</li><li>Middleton</li><li>Garden City</li><li>Kuna</li><li>Emmett</li></ul>
  <svg class="abs" style="left:9px;top:2789px" width="110" height="130" viewBox="0 0 110 130" role="img" aria-label="Street map of the service region in a hexagon frame">
    <defs><linearGradient id="mapM" x1="0" y1="0" x2="1" y2="1"><stop offset="0" stop-color="#e8e4dc"/><stop offset="1" stop-color="#d6dde3"/></linearGradient></defs>
    <polygon points="55,0 110,32 110,98 55,130 0,98 0,32" fill="url(#mapM)"/>
  </svg>

  <footer class="abs" style="left:0;top:2948px;width:131px;height:578px;background:var(--slate)">
    <svg class="abs" style="left:0;top:0" width="131" height="22" viewBox="0 0 131 22"><polygon points="0,0 131,0 131,1 65,21 0,1" fill="#fff"/></svg>
    <div class="brand" style="left:15px;top:74px;width:100px;font-size:13px;color:var(--white)">KELBROOK<div style="font-size:4px;letter-spacing:2px">LLC</div></div>
    <div class="foot-h" style="left:17px;top:124px;font-size:7px">Contact Us</div>
    <svg class="abs" style="left:17px;top:153px" width="7" height="9" viewBox="0 0 8 10"><path d="M4 10C1 6 0 4.5 0 3.5a4 4 0 0 1 8 0C8 4.5 7 6 4 10Z" fill="var(--blue)"/></svg>
    <div class="foot-t" style="left:34px;top:150px;font-size:5.5px">Loremu suodu dummy<br>984 dummy 094 dumm<br>Stree lor 6849</div>
    <svg class="abs" style="left:17px;top:200px" width="7" height="8" viewBox="0 0 8 9"><path d="M1 0.5L3 0.5L3.6 2.6L2.6 3.4C3.1 4.7 4 5.6 5.3 6.1L6.1 5.1L8 5.7L8 7.7C4 8.5 0 4.5 1 0.5Z" fill="var(--blue)"/></svg>
    <div class="foot-t" style="left:34px;top:198px;font-size:5.5px">Phone:<br>0 5550 1473 286<br>0 5550 1473 287</div>
    <div class="foot-h" style="left:17px;top:255px;font-size:7px">Links</div>
    <div class="foot-t" style="left:17px;top:280px;width:70px;font-size:5.5px">Lorem ipsum dol amet, consectetur dd do eiusmod tiempor lorem ncididunt ut labor get dol magna aliquipsum disse ultricida.</div>
    <div class="foot-h" style="left:17px;top:390px;font-size:7px">Newsletter</div>
    <div class="field" style="left:15px;top:416px;width:100px;height:18px;padding-left:10px;font-size:5px">Username</div>
    <div class="field" style="left:15px;top:443px;width:100px;height:18px;padding-left:10px;font-size:5px">Email</div>
    <div class="pill" style="left:15px;top:474px;width:100px;height:20px;font-size:5.5px">SUBMIT HERE</div>
    <div class="foot-t" style="left:0;top:526px;width:131px;text-align:center;font-size:5px">© Copyright ® 2022<br>All rights reserved.</div>
  </footer>
</main>

</body>
</html>
```